Remodeling brochure

We need an informative homeowner friendly brochure detailing our company and things we do. We are looking for an initial setup and ideas (# of pages, etc) and then we will send more content. We are uploading our logo design. We are a high end remodeling company specializing in kitchen & bath remodels. We sell ourselves on customer communication and attention to detail in our designs and remodels.

Target Market(s)

Residential homeowners

Contact Information for Business Card

Modern and attention grabbing

Requirements
Must have
• Name- Hearth & Tile Crafters<br/>Address- 728 NW Folley Lane Suite #217<br/> Ankeny, Iowa 50388<br/>Phone- 515-472-8093<br/>email-htcrafterspro@mailvane.net

```html
<!DOCTYPE html>
<html lang="en">
<head>
<meta charset="utf-8">
<title>Hearth &amp; Tile Crafters Brochure</title>
<link href="https://fonts.googleapis.com/css2?family=Montserrat:wght@400;500;600;700;800&display=swap" rel="stylesheet">
<style>
  :root {
    --bg: #3d3d3d;
    --paper: #f7f7f7;
    --ink: #2b2b2b;
    --muted: #6a6a6a;
    --blue: #1a6fd6;
    --blue-deep: #0d4fc4;
    --sky: #2a97e6;
    --teal: #0b7d86;
    --photo-warm: #d8cdbf;
    --photo-light: #e9e6e1;
  }
  * { box-sizing: border-box; margin: 0; padding: 0; }
  html, body { width: 1200px; height: 824px; overflow: hidden; }
  body { background: var(--bg); font-family: "Montserrat", sans-serif; color: var(--ink); }

  .spread { position: absolute; left: 60px; top: 30px; width: 1080px; height: 764px; display: flex; }
  .page { position: relative; width: 540px; height: 764px; background: var(--paper); overflow: hidden; }
  .page--back { box-shadow: inset -14px 0 22px -18px rgba(0,0,0,.35); }
  .page--front { box-shadow: inset 14px 0 22px -18px rgba(0,0,0,.35); }

  .spread-art { position: absolute; left: 0; top: 0; width: 1080px; height: 764px; pointer-events: none; }

  .feature-photo { position: absolute; left: 60px; top: 90px; width: 380px; height: 230px;
    background: linear-gradient(120deg, #b98b62 0%, var(--photo-warm) 40%, var(--photo-light) 75%, #f2efe9 100%); }
  .accent-teal { position: absolute; left: 400px; top: 150px; width: 80px; height: 110px; background: var(--teal); opacity: .92; }
  .accent-frame { position: absolute; left: 390px; top: 100px; width: 140px; height: 200px; border: 1px solid var(--blue-deep); }

  .section-title { font-size: 17px; font-weight: 700; letter-spacing: .5px; text-transform: uppercase; }
  .section-title span { color: var(--sky); }
  .why { position: absolute; left: 80px; top: 370px; width: 300px; }
  .why p { margin-top: 8px; font-size: 8.5px; line-height: 1.45; color: var(--muted); }
  .ticks { list-style: none; margin-top: 14px; }
  .ticks li { font-size: 10px; line-height: 1.55; display: flex; align-items: center; gap: 7px; }
  .ticks svg { width: 9px; height: 9px; }

  .contact { position: absolute; left: 80px; top: 540px; width: 320px; }
  .contact-list { list-style: none; margin-top: 12px; border-left: 1px solid var(--sky); margin-left: 5px; padding-left: 14px; }
  .contact-list li { position: relative; font-size: 10.5px; line-height: 1.4; margin-bottom: 9px; color: var(--ink); }
  .contact-list li::before { content: ""; position: absolute; left: -19px; top: 3px; width: 9px; height: 9px; border-radius: 50%; background: var(--paper); border: 1.5px solid var(--sky); }

  .brand { display: flex; align-items: center; gap: 8px; font-weight: 700; color: var(--blue); }
  .brand-mark { width: 16px; height: 16px; background: var(--blue); }
  .brand--small { position: absolute; left: 300px; top: 680px; font-size: 11px; }
  .brand--small .brand-mark { width: 12px; height: 12px; }
  .brand--large { position: absolute; left: 0; right: 0; top: 42px; justify-content: center; font-size: 21px; }
  .brand--large .brand-mark { width: 26px; height: 26px; }

  .tagline-main { font-family: "Montserrat", sans-serif; font-size: 17px; font-weight: 800; letter-spacing: 2px; fill: #fff; }
  .tagline-sub { font-family: "Montserrat", sans-serif; font-size: 11px; font-weight: 400; letter-spacing: .4px; fill: #fff; }
  .site { position: absolute; left: 540px; width: 540px; top: 690px; text-align: center; font-size: 9px; letter-spacing: 3px; color: var(--muted); }
</style>
</head>
<body>
  <main class="spread">
    <section class="page page--back">
      <div class="feature-photo" role="img" aria-label="Photo of a bright open dining room with wooden table, white chairs and kitchen island"></div>
    </section>
    <section class="page page--front">
      <div class="brand brand--large"><span class="brand-mark"></span>Hearth &amp; Tile Crafters</div>
    </section>

    <svg class="spread-art" viewBox="0 0 1080 764">
      <defs>
        <linearGradient id="interior" x1="0" y1="0" x2="1" y2="1">
          <stop offset="0" stop-color="#8f7a66"/>
          <stop offset=".4" stop-color="#d9d4cc"/>
          <stop offset="1" stop-color="#eeece8"/>
        </linearGradient>
        <linearGradient id="band" x1="0" y1="0" x2="1" y2="0">
          <stop offset="0" stop-color="#1a7fe0"/>
          <stop offset="1" stop-color="#0b4fcc"/>
        </linearGradient>
      </defs>
      <polygon role="img" aria-label="Photo of a modern open kitchen and living room with pendant lights, large windows and marble counters" points="440,110 1000,110 1000,440 700,505 440,560" fill="url(#interior)"/>
      <polygon points="440,560 700,505 1000,440 1000,540 700,610 440,665" fill="url(#band)"/>
      <polygon points="440,560 590,528 590,640 440,665" fill="var(--sky)" opacity=".55"/>
      <g class="tagline" transform="rotate(-12.1 975 490)">
        <text class="tagline-main" x="975" y="484" text-anchor="end">WE SPECIALIZE IN</text>
        <text class="tagline-sub" x="975" y="504" text-anchor="end">KITCHEN AND BATHROOM RENOVATIONS</text>
      </g>
    </svg>

    <div class="accent-frame"></div>
    <div class="accent-teal"></div>

    <div class="why">
      <h2 class="section-title">Why <span>Choose Us</span></h2>
      <p>The number one reason why you should partner with us is that we are the only company in the state licensed to do warranty work. With us, you can be confident that your projects are in safe, dependable hands. Here are more reasons to choose us:</p>
      <ul class="ticks">
        <li><svg viewBox="0 0 10 10"><path d="M1 5l3 3 5-7" fill="none" stroke="#1a6fd6" stroke-width="1.8"/></svg>Fully Insured and Licensed Business</li>
        <li><svg viewBox="0 0 10 10"><path d="M1 5l3 3 5-7" fill="none" stroke="#1a6fd6" stroke-width="1.8"/></svg>Listed on Local Pro Registry</li>
        <li><svg viewBox="0 0 10 10"><path d="M1 5l3 3 5-7" fill="none" stroke="#1a6fd6" stroke-width="1.8"/></svg>Serves Residential and Commercial Clients</li>
        <li><svg viewBox="0 0 10 10"><path d="M1 5l3 3 5-7" fill="none" stroke="#1a6fd6" stroke-width="1.8"/></svg>Various Payment Options Accepted</li>
      </ul>
    </div>

    <div class="contact">
      <h2 class="section-title">Contact <span>Info</span></h2>
      <ul class="contact-list">
        <li>728 NW Folley Lane Suite #217<br>Ankeny, Iowa 50388</li>
        <li>515-472-8093</li>
        <li>htcrafterspro@mailvane.net</li>
        <li>www.htcraftersia.com</li>
      </ul>
    </div>

    <div class="brand brand--small"><span class="brand-mark"></span>Hearth &amp; Tile Crafters</div>

    <div class="site">www.htcraftersia.com</div>
  </main>
</body>
</html>
```